New Stationary and Logo Design for Start Up Company

We need a logo design and stationary set including letterhead, business card (double sided), compliments slip and envelope for a new company Bright Lantern Media.
The files should be editable to update address and standard contact details, will need to forward to web designer and stationary printer.
The company will be an online marketer and distributer of various business education products in Australia.
The designs should convey simple clean image
Target Market(s)
Small business owners and professional service providers (ie Accountants, Lawyers, Real Estate Agents) in Australia
Industry/Entity Type
Education
Look and feel
Each slider illustrates characteristics of the customer's brand and the style your logo design should communicate.

```html
<!DOCTYPE html>
<html lang="en">
<head>
<meta charset="utf-8">
<title>Bright Lantern Media – Stationery Set</title>
<link rel="stylesheet" href="https://fonts.googleapis.com/css2?family=Open+Sans:wght@400;700&display=swap">
<style>
  :root{
    --navy:#283a78;
    --red:#d22630;
    --white:#ffffff;
    --ink:#1a1a1a;
    --shadow:4px 5px 6px rgba(0,0,0,.35);
  }
  *{margin:0;padding:0;box-sizing:border-box}
  html,body{width:1200px;height:900px;overflow:hidden;background:var(--white)}
  body{position:relative;font-family:"Open Sans",Arial,sans-serif;color:var(--ink)}
  .sheet{position:absolute;background:var(--white);box-shadow:var(--shadow);border:1px solid #555;overflow:hidden}
  .sheet svg{position:absolute;left:0;top:0;display:block}
  .brand{position:absolute;font-weight:700;letter-spacing:.16em;white-space:nowrap;text-transform:uppercase}
  .brand--light{color:var(--white)}
  .brand--navy{color:var(--navy);font-weight:400}
  .person{position:absolute;color:var(--red);font-weight:700;letter-spacing:.3em;white-space:nowrap}
  .contact{position:absolute;font-weight:700;font-size:8px;line-height:11.5px;letter-spacing:.12em;white-space:nowrap}
  .contact--center{text-align:center}
  .contact p+p.gap{margin-top:6px}

  /* letterhead */
  .letterhead{left:36px;top:68px;width:546px;height:770px}
  .letterhead .brand{left:32px;top:48px;font-size:14px}
  .letterhead .person{left:382px;top:68px;font-size:11px}
  .letterhead .contact{left:404px;top:654px;width:110px}
  .letterhead .foot-band{position:absolute;left:0;bottom:0;width:100%;height:23px;background:var(--navy)}

  /* business card */
  .card-front{left:621px;top:69px;width:259px;height:148px}
  .card-front .brand{left:0;width:100%;text-align:center;top:66px;font-size:11px;padding-left:30px}
  .card-back{left:907px;top:69px;width:259px;height:148px}
  .card-back .contact{top:42px;font-size:8px;line-height:13px}
  .card-back .contact--phone{left:24px;text-align:right;width:110px}
  .card-back .contact--address{left:147px}
  .card-back .name-band{position:absolute;left:0;bottom:0;width:100%;height:27px;background:var(--navy);color:var(--white);font-weight:700;font-size:9px;letter-spacing:.3em;text-align:center;line-height:27px}

  /* compliments slip */
  .slip{left:609px;top:321px;width:560px;height:272px}
  .slip .brand{left:26px;top:42px;font-size:14px}
  .slip .person{left:392px;top:71px;font-size:11px}
  .slip .greeting{position:absolute;left:26px;top:115px;font-size:21px;color:var(--red);letter-spacing:.06em}
  .slip .contact{left:404px;top:181px;width:110px}

  /* envelope */
  .envelope{left:612px;top:678px;width:556px;height:137px;box-shadow:0 4px 8px rgba(0,0,0,.3);border:none}
  .envelope .brand{left:10px;top:56px;font-size:13px}
  .envelope .divider{position:absolute;top:8px;width:3px;height:120px;background:linear-gradient(to bottom,rgba(210,38,48,0),var(--red) 50%,rgba(210,38,48,0))}
  .envelope .divider--one{left:260px}
  .envelope .divider--two{left:417px}
  .envelope .person{left:271px;top:61px;font-size:14px;letter-spacing:.2em}
  .envelope .contact{left:428px;top:26px;font-size:9.5px;line-height:14px}
</style>
</head>
<body>

<section class="sheet letterhead" aria-label="Letterhead">
  <svg width="546" height="114" viewBox="0 0 546 114">
    <polygon points="0,0 369,0 219,114 0,114" fill="var(--navy)"/>
    <polygon points="369,0 409,0 264,114 219,114" fill="var(--red)"/>
    <polygon points="419,0 454,0 304,114 272,114" fill="var(--navy)"/>
  </svg>
  <div class="brand brand--light">Bright Lantern Media</div>
  <div class="person">Daniel Hartley</div>
  <div class="contact contact--center">
    <p>hello@brightmail.com</p>
    <p>www.brightsite.com</p>
    <p>0198765432</p>
    <p class="gap">42 Lanternway Road</p>
    <p>Bayview</p>
    <p>Australia</p>
  </div>
  <div class="foot-band"></div>
</section>

<section class="sheet card-front" aria-label="Business card front">
  <svg width="259" height="148" viewBox="0 0 259 148">
    <rect x="0" y="0" width="259" height="121" fill="var(--navy)"/>
    <polygon points="0,80 70,121 56,121 0,92" fill="var(--red)"/>
    <polygon points="0,92 56,121 40,121 0,99" fill="var(--white)"/>
    <polygon points="0,99 40,121 24,121 0,107" fill="var(--navy)"/>
    <polygon points="0,107 24,121 0,121" fill="var(--white)"/>
  </svg>
  <div class="brand brand--light">Bright Lantern Media</div>
</section>

<section class="sheet card-back" aria-label="Business card back">
  <svg width="259" height="148" viewBox="0 0 259 148">
    <polygon points="201,121 217,121 259,97 259,87" fill="var(--red)"/>
  </svg>
  <div class="contact contact--phone">
    <p>0198765432</p>
    <p>www.brightsite.com</p>
    <p>hello@brightmail.com</p>
  </div>
  <div class="contact contact--address">
    <p>42 Lanternway Road</p>
    <p>Bayview</p>
    <p>Australia</p>
  </div>
  <div class="name-band">Daniel Hartley</div>
</section>

<section class="sheet slip" aria-label="Compliments slip">
  <svg width="560" height="111" viewBox="0 0 560 111">
    <polygon points="0,0 361,0 213,111 0,111" fill="var(--navy)"/>
    <polygon points="361,0 403,0 258,111 213,111" fill="var(--red)"/>
    <polygon points="413,0 441,0 296,111 268,111" fill="var(--navy)"/>
  </svg>
  <div class="brand brand--light">Bright Lantern Media</div>
  <div class="person">Daniel Hartley</div>
  <div class="greeting">with compliments</div>
  <div class="contact contact--center">
    <p>hello@brightmail.com</p>
    <p>www.brightsite.com</p>
    <p>0198765432</p>
    <p class="gap">42 Lanternway Road</p>
    <p>Bayview</p>
    <p>Australia</p>
  </div>
</section>

<section class="sheet envelope" aria-label="Envelope">
  <div class="brand brand--navy">Bright Lantern Media</div>
  <div class="divider divider--one"></div>
  <div class="person">Daniel Hartley</div>
  <div class="divider divider--two"></div>
  <div class="contact">
    <p>hello@brightmail.com</p>
    <p>www.brightsite.com</p>
    <p>0198765432</p>
    <p class="gap">42 Lanternway Road</p>
    <p>Bayview</p>
    <p>Australia</p>
  </div>
</section>

</body>
</html>
```